Voyage Wellcare Hub Business Cards

We need business cards for our new start-up online travel health clinic. Visit our website voyagewellcarehub.ca for branding and more info.

Target Market(s)

Travellers

Industry/Entity Type

Business

Contact Information for Business Card

Maya Koslowski
maya@voyagewellcarehub.ca
+1 555 283 6194
voyagewellcarehub.ca

Font styles to use
Sans Serif

Colors
f68d4d

```html
<!DOCTYPE html>
<html lang="en">
<head>
<meta charset="utf-8">
<title>Voyage Wellcare Hub Business Cards</title>
<link rel="stylesheet" href="https://fonts.googleapis.com/css2?family=Lato:ital,wght@0,400;1,400&family=Roboto:wght@400;500&display=swap">
<style>
  :root {
    --backdrop: #ebe6de;
    --card-dark: #1e1e1e;
    --card-grey: #b4b4b6;
    --brand-orange: #f68d4d;
    --text-light: #d0d0d0;
    --text-mid: #b9b9b9;
    --text-dark: #1c1c1c;
    --rule: #4a4a4a;
    --band-light: #fbf8f5;
  }
  * { margin: 0; padding: 0; box-sizing: border-box; }
  html, body { width: 1200px; height: 900px; overflow: hidden; }
  body { background: var(--backdrop); position: relative; font-family: "Lato", sans-serif; }

  .card {
    position: absolute; top: 306px; width: 437px; height: 271px;
    border-radius: 12px; overflow: hidden;
    box-shadow: 0 3px 8px rgba(0,0,0,0.25);
  }
  .card--front { left: 150px; background: var(--card-dark); }
  .card--back { left: 611px; background: var(--card-grey); }

  .brand {
    position: absolute; right: 22px; text-align: right;
  }
  .brand__name {
    font-family: "Lato", sans-serif; font-weight: 400;
    font-size: 27px; line-height: 1; white-space: nowrap;
  }
  .brand__tagline {
    font-family: "Lato", sans-serif; font-style: italic;
    font-size: 12.5px; margin-top: 5px;
  }
  .card--front .brand { top: 72px; }
  .card--front .brand__name { color: var(--brand-orange); }
  .card--front .brand__tagline { color: var(--text-mid); }

  .holder {
    position: absolute; left: 23px; top: 158px;
    font-family: "Roboto", sans-serif; font-weight: 500;
    font-size: 18px; letter-spacing: 0.3px; text-transform: uppercase;
    color: var(--text-mid);
  }
  .holder__first { color: var(--brand-orange); }
  .holder-rule {
    position: absolute; left: 23px; right: 22px; top: 188px;
    height: 1px; background: var(--rule);
  }
  .contacts {
    position: absolute; left: 23px; top: 198px; list-style: none;
    font-size: 13px; color: var(--text-light);
  }
  .contacts li { display: flex; align-items: center; height: 16px; }
  .contacts svg { width: 10px; height: 10px; margin-right: 5px; fill: var(--brand-orange); }

  .back-art { position: absolute; inset: 0; }
  .card--back .brand { top: 192px; right: 30px; }
  .card--back .brand__name { color: var(--text-dark); font-size: 28px; }
  .card--back .brand__tagline { color: var(--text-dark); font-size: 11.5px; margin-top: 4px; }
</style>
</head>
<body>

  <section class="card card--front">
    <div class="brand">
      <div class="brand__name">Voyage Wellcare Hub</div>
      <div class="brand__tagline">Online Travel Health Experts</div>
    </div>

    <div class="holder"><span class="holder__first">Maya</span> Koslowski</div>
    <div class="holder-rule"></div>

    <ul class="contacts">
      <li>
        <svg viewBox="0 0 10 10"><path d="M1 2.5C1 1.5 2 1 5 1s4 .5 4 1.5V4H7V3H3v1H1z M2 5h6l1 4H1z"/></svg>
        +1 555 283 6194
      </li>
      <li>
        <svg viewBox="0 0 10 10"><path d="M0 2h10v6H0z" /><path d="M0 2l5 3.5L10 2" stroke="#1e1e1e" stroke-width="1" fill="none"/></svg>
        maya@voyagewellcarehub.ca
      </li>
      <li>
        <svg viewBox="0 0 10 10"><circle cx="5" cy="5" r="4.5"/></svg>
        www.voyagewellcarehub.ca
      </li>
    </ul>
  </section>

  <section class="card card--back">
    <svg class="back-art" viewBox="0 0 437 271" preserveAspectRatio="none">
      <polygon points="0,0 255,0 0,271" fill="var(--brand-orange)"/>
      <polygon points="255,0 278,0 52,271 0,271 0,260"
               fill="var(--band-light)" role="img"
               aria-label="Large white aircraft illustration crossing the card diagonally"/>
    </svg>
    <div class="brand">
      <div class="brand__name">Voyage Wellcare Hub</div>
      <div class="brand__tagline">Online Travel Health Experts</div>
    </div>
  </section>

</body>
</html>
```